Pull Up Banner - Recruitment Company

We would like a design for a pull up banner.

For context: we are a recruitment business. We specialise in helping people in healthcare industry to find jobs in Australia.

I have come up with several ideas and text for the banner. Feel free to use the following as you see appropriate:

- Our logo (see attached)
- 'Healthcare Recruitment Agency'
- Some sort of imagine / cartoon of medical professionals (ie. doctor, nurse, physiotherapist, speech pathologist). A cartoon is more friendly than committing to a photo
- 'Empowering your next career move'
- 'Discover tailored opportunities based on your career preferences'
- Dot points (allied health, nursing, medical imaging)
- Contact info at the bottom including our website (www.quellstaffing.com.au, our Instagram handle @quellstaffing, Mobile: XXXX XXX XXX. The title section for contact information could be 'Get in touch:'

Feel free to submit a couple of designs and we can merge aspects that look good on your designs and find the perfect fit.
Thank you
Updates

Hello,

Thank you for your initial submissions to this project. I appreciate the time you've invested.

After reviewing the first attempt, I'd like to share some feedback and initial observations:

- Professionalism and engagement: Is the overall appearance of the banner professional? It's crucial that we have a high-quality design as this will represent our business.

- Image selection: The image (whether cartoon or real people) appears quite generic. Please consider submitting the banner with a few different photos in the middle for us to choose from. Ensure the image is a good fit and not simply a generic stock photo.

- Contact section: Kindly remove the phone number; we no longer wish to include it on the banner. Instead, please include our website (www.quellstaffing.com.au) and Instagram handle (@quellstaffing).

- Color scheme: White, black, and red/pink are preferred, or alternatively, blue. However, please avoid incorporating too many different colors as it may detract from the professional appearance.

We will be printing the design on a banner and require it to look professional and engaging.

Thank you once again for your submissions. I hope the feedback provided above is helpful.

Warm regards,

Target Market(s)

Allied Health Australia

Font styles to use
Serif

Colors
0054AA
0677BA
7BADD7
CADEEF
E8F1F8
0094D4
00A9DD
6FCCEA
C7EBF8
E9F6FB
EB3D1F
EC4F4E
F09395
F8D3D4
FCEDEE

```html
<!DOCTYPE html>
<html lang="en">
<head>
<meta charset="utf-8">
<title>Quell Staffing – Pull Up Banner</title>
<link rel="stylesheet" href="https://fonts.googleapis.com/css2?family=Exo+2:ital,wght@0,700;1,300;1,700&family=Saira:wght@400;600;700&display=swap">
<style>
  :root {
    --page-bg: #eeeeee;
    --white: #ffffff;
    --ink: #111111;
    --brand-blue: #0677ba;
    --deep-blue: #0562a5;
    --brand-red: #eb3d1f;
    --photo-grey: #dcdde0;
    --scrub-blue: #3a88d4;
    --skin-tone: #e9c3ad;
    --strip-grey: #e6e6e6;
    --pill-orange: #f28a21;
    --accent-yellow: #e8c21a;
  }
  html, body {
    margin: 0;
    width: 950px;
    height: 1200px;
    overflow: hidden;
    background: var(--page-bg);
  }
  .banner {
    position: absolute;
    left: 215px;
    top: 21px;
    width: 520px;
    height: 1158px;
    display: block;
  }
  .brand-name { font-family: "Exo 2", sans-serif; font-weight: 700; fill: var(--ink); }
  .headline { font-family: "Exo 2", sans-serif; font-weight: 700; font-style: italic; fill: var(--white); }
  .tagline { font-family: "Exo 2", sans-serif; font-weight: 700; font-style: italic; fill: var(--white); }
  .subline { font-family: "Exo 2", sans-serif; font-weight: 300; font-style: italic; fill: var(--white); }
  .pill-label { font-family: "Saira", sans-serif; font-weight: 600; fill: var(--white); }
  .contact-title { font-family: "Saira", sans-serif; font-weight: 400; fill: var(--accent-yellow); }
  .contact-line { font-family: "Saira", sans-serif; font-weight: 600; fill: var(--white); }
</style>
</head>
<body>
<svg class="banner" viewBox="0 0 676 1505" xmlns="http://www.w3.org/2000/svg">
  <defs>
    <radialGradient id="portrait-tones" cx="0.47" cy="0.62" r="0.45">
      <stop offset="0" stop-color="var(--scrub-blue)"/>
      <stop offset="0.45" stop-color="var(--scrub-blue)" stop-opacity="0.75"/>
      <stop offset="0.75" stop-color="var(--skin-tone)" stop-opacity="0.35"/>
      <stop offset="1" stop-color="var(--photo-grey)" stop-opacity="0"/>
    </radialGradient>
  </defs>

  <!-- base -->
  <rect width="676" height="1505" fill="var(--white)"/>
  <rect y="30" width="676" height="12" fill="var(--strip-grey)"/>

  <!-- brand -->
  <text class="brand-name" x="45" y="165" font-size="50" letter-spacing="3">QUELL STAFFING</text>

  <!-- photo area -->
  <g role="img" aria-label="Photo of a smiling nurse in blue scrubs with a stethoscope giving two thumbs up">
    <polygon points="0,595 676,340 676,1100 0,1360" fill="var(--photo-grey)"/>
    <polygon points="0,595 676,340 676,1100 0,1360" fill="url(#portrait-tones)"/>
  </g>

  <!-- top accent stripes -->
  <polygon points="0,310 308,223 250,246 0,343" fill="var(--brand-red)"/>
  <polygon points="0,367 676,112 676,318 0,570" fill="var(--brand-blue)"/>
  <polygon points="0,570 676,318 676,340 0,595" fill="var(--white)"/>

  <!-- service badge -->
  <ellipse cx="578" cy="520" rx="40" ry="36" fill="none" stroke="var(--accent-yellow)" stroke-width="2"/>

  <!-- headline -->
  <text class="headline" font-size="72" transform="translate(160,405) rotate(-20.6)">Healthcare</text>
  <text class="headline" font-size="56" transform="translate(86,492) rotate(-20.6)">Recruitment Agency</text>

  <!-- lower bands -->
  <polygon points="0,1150 676,895 676,1505 0,1505" fill="var(--brand-blue)"/>
  <polygon points="0,1150 676,895 676,1060 0,1315" fill="var(--brand-red)"/>
  <polygon points="0,1342 306,1255 220,1290 0,1375" fill="var(--brand-red)"/>
  <rect y="1465" width="676" height="10" fill="var(--deep-blue)"/>
  <rect y="1475" width="676" height="30" fill="var(--white)"/>

  <!-- tagline -->
  <text class="tagline" font-size="33" transform="translate(72,1180) rotate(-20.6)">Empowering your next career move</text>
  <text class="subline" font-size="28" transform="translate(102,1218) rotate(-20.6)">Discover tailored opportunities based on</text>
  <text class="subline" font-size="28" transform="translate(194,1222) rotate(-20.6)">your career preferences'</text>

  <!-- specialties -->
  <rect x="385" y="1188" width="247" height="37" rx="18.5" fill="var(--pill-orange)"/>
  <text class="pill-label" x="608" y="1216" font-size="26" text-anchor="end">ALLIED HEALTH</text>
  <rect x="436" y="1235" width="196" height="37" rx="18.5" fill="var(--pill-orange)"/>
  <text class="pill-label" x="608" y="1263" font-size="26" text-anchor="end">NURSING</text>
  <rect x="336" y="1287" width="296" height="37" rx="18.5" fill="var(--pill-orange)"/>
  <text class="pill-label" x="608" y="1315" font-size="26" text-anchor="end">MEDICAL IMAGING</text>

  <!-- contact -->
  <text class="contact-title" x="90" y="1400" font-size="17">Get in touch</text>
  <g fill="none" stroke="var(--white)" stroke-width="1.8">
    <circle cx="225" cy="1377" r="8"/>
    <ellipse cx="225" cy="1377" rx="3.5" ry="8"/>
    <line x1="217" y1="1377" x2="233" y2="1377"/>
    <circle cx="225" cy="1410" r="8"/>
  </g>
  <text class="contact-line" x="251" y="1384" font-size="22">www.quellstaffing.com.au,</text>
  <text class="contact-line" x="251" y="1417" font-size="22">@quellstaffing</text>
</svg>
</body>
</html>
```